its a new company based in Christchurch new Zealand building computers ,repairs, upgrades and anything computers for the general public,i like bright happy colours like yellows, greens reds anything that stands out and it needs to communicant trust and security towards my new company,i have no logo yet,

Target Market(s)

target market of all ages

Industry/Entity Type

Building

Contact Information for Business Card

Pixel Harbour Limited,ph-0214862735,email-bluefoxtrail17@mailnest.example,4c marlowe rd,fernvale

```html
<!DOCTYPE html>
<html lang="en">
<head>
<meta charset="utf-8">
<title>Pixel Harbour Limited – Business Card</title>
<link rel="stylesheet" href="https://fonts.googleapis.com/css2?family=Questrial&family=Open+Sans:wght@800&display=swap">
<style>
  :root {
    --card-white: #ffffff;
    --brand-red: #b00000;
    --brand-grey: #c3ccca;
    --ink: #111111;
  }
  * { margin: 0; padding: 0; box-sizing: border-box; }
  html, body {
    width: 1200px;
    height: 741px;
    overflow: hidden;
    background: var(--card-white);
  }
  .card {
    position: relative;
    width: 1200px;
    height: 741px;
    background: var(--card-white);
    overflow: hidden;
  }
  .side-band {
    position: absolute;
    left: 0;
    top: 0;
    width: 71px;
    height: 741px;
    background: var(--brand-grey);
  }
  .corner-decoration {
    position: absolute;
    right: 0;
    bottom: 0;
    width: 470px;
    height: 520px;
    background: radial-gradient(circle at 100% 100%,
      var(--brand-red) 0%,
      rgba(176, 0, 0, 0.55) 30%,
      rgba(195, 204, 202, 0.6) 55%,
      rgba(255, 255, 255, 0) 75%);
  }
  .brand {
    position: absolute;
    left: 470px;
    top: 140px;
    display: flex;
    align-items: center;
    gap: 30px;
  }
  .brand__square {
    width: 80px;
    height: 80px;
    background: var(--brand-grey);
    flex: none;
  }
  .brand__name {
    font-family: "Questrial", "Century Gothic", sans-serif;
    font-weight: 400;
    font-size: 68px;
    line-height: 1.05;
    color: var(--brand-red);
  }
  .contact {
    position: absolute;
    left: 103px;
    top: 438px;
    list-style: none;
    font-family: "Open Sans", Verdana, sans-serif;
    font-weight: 800;
    font-size: 30px;
    line-height: 43px;
    color: var(--ink);
  }
</style>
</head>
<body>
  <main class="card">
    <div class="side-band"></div>

    <div class="corner-decoration" role="img" aria-label="Soft red and grey corner decoration"></div>

    <div class="brand">
      <div class="brand__square"></div>
      <h1 class="brand__name">Pixel Harbour<br>Limited</h1>
    </div>

    <ul class="contact">
      <li class="contact__phone">PH-0214862735</li>
      <li class="contact__email">email-bluefoxtrail17@mailnest.example</li>
      <li class="contact__street">4c Marlowe RD</li>
      <li class="contact__suburb">Fernvale</li>
    </ul>
  </main>
</body>
</html>
```